Proposal Poster, posters for kids to hold

I am proposing to my girlfriend soon, I need two posters made for my kids to hold one I want to say “be my mommy”
And the other “will you marry my daddy”
Both in horizontal format. I plan on sending the files to a print shop to get them printed on a large poster. Simple is fine with maybe a few graphics. Open to anything. Kids will be holding it from the beach as we are on a jet ski close to shore. Must be readable font from a short distance

• Cute but readable font from a distance

```html
<!DOCTYPE html>
<html lang="en">
<head>
<meta charset="utf-8">
<title>Will you marry my Daddy? – Proposal Poster</title>
<link rel="stylesheet" href="https://fonts.googleapis.com/css2?family=Playball&display=swap">
<style>
  :root {
    --page-bg: #ffffff;
    --plum-top: #5a0d50;
    --plum-mid: #520c45;
    --wine-bottom: #6e0f2a;
    --ink-white: #ffffff;
    --gold-light: #f0cf6e;
    --gold-deep: #d9ad45;
    --gold-soft: rgba(230, 191, 90, 0.38);
  }
  * { margin: 0; padding: 0; box-sizing: border-box; }
  html, body {
    width: 820px;
    height: 1200px;
    overflow: hidden;
    background: var(--page-bg);
  }
  .canvas {
    position: relative;
    width: 820px;
    height: 1200px;
  }
  .poster {
    position: absolute;
    left: 55px;
    top: 334px;
    width: 710px;
    height: 530px;
    overflow: hidden;
    background: linear-gradient(180deg, var(--plum-top) 0%, var(--plum-mid) 45%, var(--wine-bottom) 100%);
  }
  .heart-field {
    position: absolute;
    left: 0;
    right: 0;
    bottom: 0;
    height: 60%;
    background: radial-gradient(ellipse at 50% 100%, rgba(160, 30, 60, 0.45) 0%, rgba(160, 30, 60, 0) 70%);
  }
  .headline {
    position: absolute;
    inset: 0;
    font-family: "Playball", cursive;
    font-weight: 400;
  }
  .line {
    position: absolute;
    white-space: nowrap;
    line-height: 1;
  }
  .line-will {
    left: 105px;
    top: 92px;
    font-size: 110px;
    color: var(--ink-white);
  }
  .line-marry {
    left: 244px;
    top: 170px;
    font-size: 98px;
    background: linear-gradient(180deg, var(--gold-light), var(--gold-deep));
    -webkit-background-clip: text;
    background-clip: text;
    color: transparent;
  }
  .line-daddy {
    left: 112px;
    top: 324px;
    font-size: 165px;
    color: var(--ink-white);
  }
  .ring-mark {
    position: absolute;
    left: 494px;
    top: 60px;
    width: 106px;
    height: 112px;
  }
  .heart-pair {
    position: absolute;
  }
  .heart-pair.small { left: 95px; top: 203px; width: 30px; height: 22px; }
  .heart-pair.large { left: 90px; top: 246px; width: 62px; height: 48px; }
</style>
</head>
<body>
  <main class="canvas">
    <section class="poster" aria-label="Proposal poster">
      <div class="heart-field" role="img" aria-label="Soft scattered red hearts pattern"></div>

      <svg class="ring-mark" role="img" aria-label="Gold wedding rings icon with heart" viewBox="0 0 106 112">
        <rect width="106" height="112" rx="50" fill="var(--gold-soft)"/>
      </svg>

      <svg class="heart-pair small" role="img" aria-label="Small gold linked hearts" viewBox="0 0 30 22">
        <rect width="30" height="22" rx="11" fill="var(--gold-soft)"/>
      </svg>
      <svg class="heart-pair large" role="img" aria-label="Gold linked hearts" viewBox="0 0 62 48">
        <rect width="62" height="48" rx="22" fill="var(--gold-soft)"/>
      </svg>

      <h1 class="headline">
        <span class="line line-will">Will you</span>
        <span class="line line-marry">marry my</span>
        <span class="line line-daddy">Daddy?</span>
      </h1>
    </section>
  </main>
</body>
</html>
```